Rising Stewards Scheme. Brochure to Inform Target Audience.

Rising Steward Scheme:

4 Page Brochure
Aimed at Parents and Children (Age 11-16)
Programme Overview
Specific Focus on Bronze Award with Learning Objectives and Enabling Objectives from Content Document
Contact Area Needed
How to Book - Online through the Website
Should encourage people to want to join it or sign up

you can use stock rugby images if needed

Target Market(s)

children between ages 11-16 and parents, gatekeepers (schools, rugby clubs)

Industry/Entity Type

Education

Font styles to use
Serif
Sans Serif

Requirements
Must have
• the programme content, each award continent and bronze award learning objectives
• Colours should match existing work that has been created
• Get in touch: www.valemark-rss.com
• maris@valemark-rss.com
Nice to have
• graphics of kids playing rugby if possible from stock images

```html
<!DOCTYPE html>
<html lang="en">
<head>
<meta charset="utf-8">
<title>Rising Stewards Scheme – Brochure Spread</title>
<link rel="stylesheet" href="https://fonts.googleapis.com/css2?family=Open+Sans:wght@400;700&family=Oswald:wght@500&family=Russo+One&display=swap">
<style>
  :root {
    --bg: #e6e6e6;
    --ink: #1a1a1a;
    --paper: #ffffff;
    --black: #0b0b0b;
    --gold: #f6c21a;
    --pitch: #2f6a2c;
    --muted: #4a4a4a;
  }
  * { box-sizing: border-box; margin: 0; padding: 0; }
  html, body { width: 1200px; height: 800px; overflow: hidden; background: var(--bg); }
  .spread { position: absolute; left: 60px; top: 20px; width: 1080px; height: 760px; display: flex; box-shadow: 0 10px 30px rgba(0,0,0,.25); }
  .page { position: relative; width: 540px; height: 760px; overflow: hidden; }

  /* Back cover */
  .back-photo { position: absolute; inset: 0;
    background: linear-gradient(160deg, #3b4a5e 0%, #6b5a3a 35%, #2d5a2a 65%, #1f3d1c 100%); }
  .faq-shape { position: absolute; inset: 0; }
  .faq-title { position: absolute; left: 40px; top: 26px; font: 400 22px "Open Sans", sans-serif; color: var(--ink); }
  .faq { position: absolute; font: 400 8.6px/1.35 "Open Sans", sans-serif; color: var(--muted); }
  .faq dt { font-weight: 700; color: var(--ink); }
  .faq dd { margin-bottom: 6px; }
  .faq-wide { left: 40px; top: 66px; width: 460px; }
  .faq-narrow { left: 258px; top: 204px; width: 262px; }
  .back-url { position: absolute; left: 40px; bottom: 30px; font: 700 12px "Open Sans", sans-serif; color: var(--paper); letter-spacing: .5px; }

  /* Front cover */
  .front-photo { position: absolute; inset: 0;
    background: radial-gradient(ellipse at 70% 20%, #c9d6d0 0%, #6e8078 30%, transparent 60%),
                radial-gradient(ellipse at 45% 30%, #55585c 0%, #2e3034 40%, transparent 65%),
                linear-gradient(180deg, #2a3a32 0%, #1c3a22 55%, #0f1a12 100%); }
  .brand-panel { position: absolute; inset: 0; }
  .brand { position: absolute; left: 360px; top: 300px; width: 170px; text-align: center; color: var(--gold); font-family: "Oswald", sans-serif; font-weight: 500; }
  .brand-mark { display: inline-block; width: 46px; height: 46px; border: 3px solid var(--gold); border-radius: 50%; margin-bottom: 6px; }
  .brand-name { font-size: 15px; letter-spacing: 1px; }
  .scheme-name { margin-top: 10px; font-size: 24px; line-height: 1; letter-spacing: .5px; }
  .scheme-sub { font-size: 13px; letter-spacing: 4px; border-top: 2px solid var(--gold); border-bottom: 2px solid var(--gold); margin-top: 4px; }
  .tile { position: absolute; border: 4px solid var(--gold); background: var(--pitch); }
  .tile-match { left: 24px; top: 318px; width: 128px; height: 112px; transform: rotate(-3deg);
    background: linear-gradient(150deg, #8fa3b0, #6b4c4c 50%, #3f6a35); }
  .tile-stadium { left: 150px; top: 334px; width: 180px; height: 140px; transform: rotate(9deg);
    background: linear-gradient(180deg, #cfd8df 0%, #8a949c 35%, #3e8a3c 60%, #2b6a2a 100%); }
  .tile-tackle { left: 350px; top: 470px; width: 150px; height: 138px; transform: rotate(10deg);
    background: linear-gradient(160deg, #a33a32, #d9d9d9 45%, #2f6a2c); }
  .headline { position: absolute; left: 30px; top: 585px; font: 400 38px/1.08 "Russo One", sans-serif; color: var(--paper); }
  .headline span { display: block; }
  .headline .l1 { padding-left: 80px; }
  .headline .l2 { padding-left: 46px; }
  .headline em { font-style: normal; color: var(--gold); }
</style>
</head>
<body>
<main class="spread">
  <section class="page back-cover">
    <div class="back-photo" role="img" aria-label="Rugby player in green catching the ball in front of a cheering crowd"></div>
    <svg class="faq-shape" viewBox="0 0 540 760" width="540" height="760" aria-hidden="true">
      <path d="M0 0 H540 V520 C460 518 310 512 262 488 C222 468 228 420 230 380 C232 320 212 262 232 226 C248 200 200 192 0 192 Z" fill="var(--paper)" stroke="var(--black)" stroke-width="9"/>
      <path d="M0 0 H540 V520 C460 518 310 512 262 488 C222 468 228 420 230 380 C232 320 212 262 232 226 C248 200 200 192 0 192 Z" fill="var(--paper)"/>
    </svg>
    <h2 class="faq-title">Frequent Asked Questions</h2>
    <dl class="faq faq-wide">
      <dt>Will you provide lunch or snacks?</dt>
      <dd>Water will be provided to refill water bottles. However, we ask that children bring their own lunch.</dd>
      <dt>Who attends your Rising Stewards Scheme?</dt>
      <dd>Children of all abilities, some who have played rugby before and some who have never played. The scheme is available to both boys and girls.</dd>
      <dt>When do I drop and pick up my child from the scheme?</dt>
      <dd>Venue timings are included in your welcome letter. Typically the drop off time is 0900 and collection time at 1600. Please ensure your child is handed over and registered to one of our coaches before you leave.</dd>
    </dl>
    <dl class="faq faq-narrow">
      <dt>What should my child wear?</dt>
      <dd>Activities will take place both indoor and outdoor, therefore please ensure you bring appropriate rugby kit, including waterproofs and a change of kit, also trainers and boots.</dd>
      <dt>What makes your scheme the right choice for my child?</dt>
      <dd>The scheme is fun and designed to develop the child's leadership skills on and off the pitch. These skills will help them grow as individuals.</dd>
      <dt>How can I enrol on the silver or gold award?</dt>
      <dd>In order to enrol on the Silver Award the child must have successfully completed the Bronze Award. In order to enrol on the Gold Award the child must have completed the Silver Award.</dd>
      <dt>Will I meet a Valemark coach?</dt>
      <dd>Yes. Whilst on the scheme you will have a chance to meet and learn from a Valemark coach.</dd>
      <dt>How do you comply with safeguarding?</dt>
      <dd>This is really important to us. We want all children to experience a fun, healthy and safe environment, therefore our coaches and staff are educated and trained in safeguarding, child protection and are all DBS checked.</dd>
    </dl>
    <p class="back-url">www.valemark-rss.com</p>
  </section>

  <section class="page front-cover">
    <div class="front-photo" role="img" aria-label="Rugby player with arms folded standing in a floodlit stadium"></div>
    <svg class="brand-panel" viewBox="0 0 540 760" width="540" height="760" aria-hidden="true">
      <path d="M540 265 C450 270 380 300 345 360 L340 590 C400 600 460 610 540 640 Z" fill="var(--black)"/>
      <path d="M540 265 C450 270 380 300 345 360" fill="none" stroke="var(--gold)" stroke-width="6"/>
      <path d="M0 300 L120 330 L340 350" fill="none" stroke="var(--gold)" stroke-width="3"/>
      <path d="M260 470 L520 640 L540 640" fill="none" stroke="var(--gold)" stroke-width="4"/>
    </svg>
    <div class="tile tile-match" role="img" aria-label="Young players running with the ball in a match"></div>
    <div class="tile tile-stadium" role="img" aria-label="Aerial view of a full rugby stadium"></div>
    <div class="tile tile-tackle" role="img" aria-label="Players contesting a tackle on the try line"></div>
    <div class="brand">
      <span class="brand-mark"></span>
      <p class="brand-name">VALEMARK RUGBY</p>
      <p class="scheme-name">RISING STEWARDS</p>
      <p class="scheme-sub">SCHEME</p>
    </div>
    <h1 class="headline">
      <span class="l1"><em>Learn</em> to Lead</span>
      <span class="l2">and <em>Play</em> the</span>
      <span class="l3">Valemark <em>Way</em></span>
    </h1>
  </section>
</main>
</body>
</html>
```